Capability Statement Document/Flyer

Take the existing words from the capability statement document (attached) and design a unique folder/flyer document for professional use. Maybe something like a trifold or bifold style. Use approved colours and logo as per the attached files.
Our company designs and builds small onshore gas processing plants.

```html
<!DOCTYPE html>
<html lang="en">
<head>
<meta charset="utf-8">
<title>Veridan Capability Statement</title>
<link rel="stylesheet" href="https://fonts.googleapis.com/css2?family=Montserrat:wght@400;500;600;700;800;900&display=swap">
<style>
:root{
  --teal:#0c7a6a;
  --teal-dark:#086657;
  --grey:#bdbdbd;
  --grey-text:#b3b3b3;
  --ink:#2f3432;
  --row:#efefef;
  --paper:#ffffff;
  --backdrop:#c9c9c9;
}
*{box-sizing:border-box;margin:0;padding:0}
html,body{width:898px;height:1200px;overflow:hidden}
body{background:var(--backdrop);font-family:'Montserrat',sans-serif;color:var(--ink);position:relative}
.page{position:absolute;width:368px;height:519px;background:var(--paper);box-shadow:0 2px 6px rgba(0,0,0,.18);overflow:hidden}
.p1{left:81px;top:72px}.p2{left:461px;top:72px}.p3{left:81px;top:608px}.p4{left:461px;top:608px}
.abs{position:absolute}
.wordmark{font-weight:800;color:var(--teal);letter-spacing:.5px;line-height:1}
.cover-mark{left:0;width:368px;top:28px;text-align:center;font-size:40px}
.cover-band{left:0;top:94px;width:368px;height:17px;background:var(--teal)}
.cover-photo{left:0;top:112px;width:368px;height:190px;background:linear-gradient(180deg,#2f73c4 0%,#5b9ad6 45%,#b98f4e 75%,#6a5a3c 100%)}
.cover-foot-band{left:0;top:302px;width:368px;height:16px;background:var(--teal)}
.cover-title{left:0;width:368px;text-align:center;font-weight:900;font-size:46px;line-height:1;letter-spacing:-1px}
.cover-title.t1{top:336px;color:var(--teal)}
.cover-title.t2{top:383px;color:var(--grey)}
.cover-tag{left:0;width:368px;top:439px;text-align:center;font-size:14px;font-weight:500;line-height:19px;color:var(--ink)}
.cover-web{left:0;width:368px;top:490px;text-align:center;font-size:10.5px;letter-spacing:3px;color:var(--teal);font-weight:500}
.globe{display:inline-block;width:9px;height:9px;border:1px solid #999;border-radius:50%;vertical-align:-1px;margin-right:5px}
.head{left:14px;font-size:14.5px;font-weight:500;color:var(--ink);border-left:1.5px solid var(--teal);padding-left:6px;line-height:14px}
.head b{color:var(--teal);font-weight:700}
.mini-mark{right:14px;top:24px;font-size:19px}
.copy{left:14px;width:340px;font-size:7.3px;line-height:10px;color:var(--ink)}
.copy b{color:var(--teal)}
.vision-top{left:14px;top:95px;width:340px;height:15px;background:var(--grey);color:#fff;font-size:8.5px;font-weight:600;text-align:center;line-height:15px}
.vision{left:14px;top:110px;width:340px;height:27px;background:var(--teal);color:#fff;font-size:11.5px;font-weight:700;display:flex;align-items:center;justify-content:center;gap:6px}
.vision .dot{width:15px;height:15px;border:1.5px solid #fff;border-radius:50%;margin-left:6px}
.principles{left:14px;top:249px;width:340px;display:flex;justify-content:space-between}
.principle{display:flex;align-items:center;gap:6px;font-size:7.3px;line-height:10px}
.ring{width:33px;height:33px;border-radius:50%;background:var(--teal);border:2px solid #fff;box-shadow:0 0 0 1.5px var(--teal);display:flex;align-items:center;justify-content:center}
.tier{left:30px;width:307px;height:35px;border-radius:18px;background:var(--teal);color:#fff;font-size:9px;font-weight:600;display:flex;align-items:center;padding-left:14px}
.tier .icon{width:18px;height:18px;margin-right:10px}
.node{position:absolute;background:#fff;color:var(--ink);border-radius:14px;height:28px;top:3.5px;display:flex;align-items:center;justify-content:center;font-size:6.6px;font-weight:600;text-align:center;line-height:8px}
.link-v{left:241px;width:1.5px;background:#fff;top:318px;height:80px;position:absolute}
.link-h{height:1.5px;background:#fff;position:absolute;top:17px}
.footer{left:14px;top:491px;width:340px;height:14px;display:flex;align-items:center}
.footer .url{font-size:10px;font-weight:600;color:var(--teal);letter-spacing:.6px;white-space:nowrap}
.footer .rule{flex:1;height:1px;background:var(--teal);margin:0 6px}
.footer .num{border:1.2px solid var(--ink);font-size:10px;font-weight:500;padding:0 3px;line-height:12px}
.table{left:14px;top:58px;width:340px}
.thead{display:grid;grid-template-columns:161px 179px;height:16px;font-size:8.5px;font-weight:700;color:#fff;line-height:16px}
.thead div:first-child{background:var(--grey);padding-left:16px}
.thead div:last-child{background:var(--teal);padding-left:20px}
.row{display:grid;grid-template-columns:161px 179px;font-size:7.2px}
.row .fn{display:flex;align-items:center;font-weight:600;line-height:9.5px}
.row .fn svg{width:14px;height:14px;margin:0 21px 0 16px;flex:none}
.row .svc{display:flex;align-items:center;padding-left:20px;line-height:9.5px}
.row.teal .fn{background:var(--teal);color:#fff}
.row.teal .svc{background:#fff}
.row.soft .fn,.row.soft .svc{background:var(--row)}
.row.soft .fn svg{color:var(--teal)}
.row.teal .fn svg{color:#fff}
.list{left:14px;width:250px;font-size:6.8px;font-weight:600;list-style:none}
.list li{display:flex;align-items:center;height:13px}
.list li i{width:7px;height:7px;border-radius:50%;margin-right:6px;flex:none}
.list.good li i{background:var(--teal)}
.list.bad li i{background:#d9262c}
.side-photo{left:266px;width:88px;height:82px}
.contact{left:14px;top:457px;width:340px;height:22px;background:var(--teal);color:#fff;font-size:9px;font-weight:700;display:flex;align-items:center;justify-content:center;gap:15px}
</style>
</head>
<body>

<!-- Cover -->
<section class="page p1">
  <div class="abs wordmark cover-mark">VERIDAN</div>
  <div class="abs cover-band"></div>
  <div class="abs cover-photo" role="img" aria-label="Photograph of an onshore gas processing plant with towers and pipework under a blue sky at sunset"></div>
  <div class="abs cover-foot-band"></div>
  <h1 class="abs cover-title t1">CAPABILITY</h1>
  <h1 class="abs cover-title t2">STATEMENT</h1>
  <p class="abs cover-tag">Simplify Project Execution,<br>Streamline Operations</p>
  <p class="abs cover-web"><span class="globe"></span>www.veridan.com.au</p>
</section>

<!-- Page 2 -->
<section class="page p2">
  <h2 class="abs head" style="top:27px">Who are <b>Veridan?</b></h2>
  <div class="abs wordmark mini-mark">VERIDAN</div>
  <p class="abs copy" style="top:57px"><b>Veridan</b> are a highly experienced team of Executive, Project, Construction, Commissioning and Operations specialists who combine deep technical knowledge with proven leadership to deliver unique Project Delivery Partner services to organisations in Australia.</p>
  <div class="abs vision-top">OUR VISION IS STRAIGHTFORWARD:</div>
  <div class="abs vision"><span class="dot"></span>Simplify Project Execution <span class="dot"></span>Streamline Operations</div>
  <h2 class="abs head" style="top:149px">What is a <b>Project Delivery Partner?</b></h2>
  <p class="abs copy" style="top:173px">A Project Delivery Partner (PDP) provides integrated project management along with technical, commercial and delivery support services to help an organisation successfully deliver a project. The PDP acts as the owner’s team while the owner retains accountability and key decision making authority.</p>
  <h2 class="abs head" style="top:226px"><b>PDP</b> Core Principles</h2>
  <div class="abs principles">
    <div class="principle"><span class="ring"><svg width="14" height="14" viewBox="0 0 14 14" fill="none" stroke="#fff" stroke-width="1.3"><rect x="2" y="2" width="10" height="10"/><path d="M4 9l2-2 2 1 2-3"/></svg></span>Owner controls<br>the project</div>
    <div class="principle"><span class="ring"><svg width="14" height="14" viewBox="0 0 14 14" fill="none" stroke="#fff" stroke-width="1.3"><path d="M7 1l5 2v4c0 3-2 5-5 6-3-1-5-3-5-6V3z"/><path d="M4.5 7l2 2 3-3"/></svg></span>PDP enables delivery<br>&amp; provides assurance</div>
    <div class="principle"><span class="ring"><svg width="14" height="14" viewBox="0 0 14 14" fill="none" stroke="#fff" stroke-width="1.3"><circle cx="7" cy="7" r="5"/><circle cx="7" cy="7" r="2"/></svg></span>Contractors execute<br>the work</div>
  </div>

  <div class="abs tier" style="top:300px"><svg class="icon" viewBox="0 0 18 18" fill="#fff"><circle cx="9" cy="5" r="3.5"/><rect x="3" y="10" width="12" height="6" rx="2"/></svg>Owner
    <div class="node" style="left:190px;width:45px">Operator<br>XYZ</div></div>
  <div class="abs tier" style="top:340px"><svg class="icon" viewBox="0 0 18 18" fill="#fff"><circle cx="9" cy="5" r="3.5"/><rect x="3" y="10" width="12" height="6" rx="2"/></svg>Project Delivery Partner
    <div class="node" style="left:190px;width:45px;font-size:7px;color:var(--teal);font-weight:800">VERIDAN</div></div>
  <div class="abs tier" style="top:381px"><svg class="icon" viewBox="0 0 18 18" fill="#fff"><circle cx="9" cy="5" r="3.5"/><rect x="3" y="10" width="12" height="6" rx="2"/></svg>Contractors
    <span class="link-h" style="left:171px;width:130px"></span>
    <div class="node" style="left:124px;width:48px">Engineering</div>
    <div class="node" style="left:190px;width:45px">Suppliers</div>
    <div class="node" style="left:251px;width:50px">Execution</div></div>
  <span class="link-v" style="left:271px;top:318px;height:80px"></span>

  <h2 class="abs head" style="top:435px"><b>PDP</b> Objective</h2>
  <p class="abs copy" style="top:458px">Deliver the project safely, on schedule, within budget and ready for operations; providing owner capability throughout the project lifecycle.</p>
  <div class="abs footer"><span class="globe"></span><span class="url">www.veridan.com.au</span><span class="rule"></span><span class="num">02</span></div>
</section>

<!-- Page 3 -->
<section class="page p3">
  <h2 class="abs head" style="top:27px"><b>PDP</b> Services</h2>
  <div class="abs wordmark mini-mark">VERIDAN</div>
  <div class="abs table">
    <div class="thead"><div>FUNCTION</div><div>VERIDAN SERVICE</div></div>
    <div class="row teal" style="height:35px"><div class="fn"><svg viewBox="0 0 14 14" fill="none" stroke="currentColor" stroke-width="1.4"><rect x="2" y="2" width="10" height="10" rx="1"/><path d="M4 5h6M4 7.5h6M4 10h4"/></svg>Project<br>Management</div><div class="svc">Planning, Reporting &amp; Delivery Leadership<br>from Concept to Completion</div></div>
    <div class="row soft" style="height:30px"><div class="fn"><svg viewBox="0 0 14 14" fill="currentColor"><path d="M2 8a5 5 0 0110 0z"/><rect x="1.5" y="8.5" width="11" height="1.5"/><circle cx="7" cy="11.5" r="1.8"/></svg>Engineering</div><div class="svc">Concept Selection, Design Coordination,<br>Technical Assurance &amp; Value Engineering</div></div>
    <div class="row teal" style="height:30px"><div class="fn"><svg viewBox="0 0 14 14" fill="none" stroke="currentColor" stroke-width="1.4"><path d="M1 2h2l2 7h7l1-5H4"/><circle cx="6" cy="12" r="1"/><circle cx="11" cy="12" r="1"/></svg>Procurement</div><div class="svc">Contracting Strategy, Tender Process &amp;<br>Supplier/Contractor Management</div></div>
    <div class="row soft" style="height:30px"><div class="fn"><svg viewBox="0 0 14 14" fill="none" stroke="currentColor" stroke-width="1.4"><rect x="2" y="1.5" width="9" height="11" rx="1"/><path d="M4 7l2 2 3-4"/></svg>Approvals</div><div class="svc">Land Access, Regulator Engagement,<br>Safety Case, Permits &amp; Licenses</div></div>
    <div class="row teal" style="height:30px"><div class="fn"><svg viewBox="0 0 14 14" fill="none" stroke="currentColor" stroke-width="1.4"><circle cx="8" cy="5" r="3.5"/><path d="M1 10l3 2h5l3-2"/></svg>Cost Control</div><div class="svc">Budget Development, Forecasting &amp;<br>Management</div></div>
    <div class="row soft" style="height:30px"><div class="fn"><svg viewBox="0 0 14 14" fill="none" stroke="currentColor" stroke-width="1.4"><rect x="1.5" y="2.5" width="9" height="9" rx="1"/><path d="M1.5 5.5h9"/><circle cx="10.5" cy="10.5" r="2.5" fill="#fff"/></svg>Scheduling</div><div class="svc">Master Schedule Development, WBS,<br>Resource Allocation, Monitoring &amp; Updating</div></div>
    <div class="row teal" style="height:32px"><div class="fn"><svg viewBox="0 0 14 14" fill="none" stroke="currentColor" stroke-width="1.4"><path d="M7 1.5l5.5 10h-11z"/><path d="M7 5.5v3M7 10v.5"/></svg>Risk Management</div><div class="svc">Risk Register, Identification, Mitigation &amp;<br>Reporting</div></div>
    <div class="row soft" style="height:30px"><div class="fn"><svg viewBox="0 0 14 14" fill="none" stroke="currentColor" stroke-width="1.4"><path d="M1.5 5L7 2l5.5 3zM3 6v5M7 6v5M11 6v5M1.5 12.5h11"/></svg>Governance</div><div class="svc">Framework, Stage Gates, Change control,<br>Reporting &amp; Decision Support</div></div>
    <div class="row teal" style="height:31px"><div class="fn"><svg viewBox="0 0 14 14" fill="none" stroke="currentColor" stroke-width="1.4"><path d="M2 7l5-4.5L12 7v5.5H2z"/><path d="M5.5 12.5v-3h3v3"/></svg>Construction</div><div class="svc">Management &amp; Coordination of Contractor<br>Execution Teams</div></div>
    <div class="row soft" style="height:39px"><div class="fn"><svg viewBox="0 0 14 14" fill="none" stroke="currentColor" stroke-width="1.4"><path d="M1 8l3-2 3 2 3-2 3 2"/><circle cx="7" cy="3.5" r="2"/><path d="M3 10l4 2.5 4-2.5"/></svg>Commissioning<br>&amp; Start-up</div><div class="svc">Lead Commissioning &amp; Start-up,<br>Completions System, Bring the Facility<br>to Steady-State</div></div>
    <div class="row teal" style="height:39px"><div class="fn"><svg viewBox="0 0 14 14" fill="none" stroke="currentColor" stroke-width="1.4"><circle cx="7" cy="7" r="5.5"/><path d="M7 3.5V7l2.5 1.5"/></svg>Operations<br>Readiness</div><div class="svc">People &amp; Organisation, Process &amp;<br>Procedures, Systems &amp; Technology</div></div>
    <div class="row soft" style="height:42px"><div class="fn"><svg viewBox="0 0 14 14" fill="none" stroke="currentColor" stroke-width="1.4"><circle cx="5.5" cy="5.5" r="3.5"/><circle cx="5.5" cy="5.5" r="1.2"/><circle cx="10.5" cy="10.5" r="2.2"/></svg>Operations &amp;<br>Maintenance</div><div class="svc">Monitor &amp; Operate Asset, Minimize<br>Downtime, Lowest Possible OPEX<br>for Owner</div></div>
  </div>
  <div class="abs footer"><span class="globe"></span><span class="url">www.veridan.com.au</span><span class="rule"></span><span class="num">03</span></div>
</section>

<!-- Page 4 -->
<section class="page p4">
  <h2 class="abs head" style="top:27px"><b>PDP Roles</b> &amp; Responsibilities</h2>
  <div class="abs wordmark mini-mark">VERIDAN</div>
  <div class="abs table">
    <div class="thead"><div>OWNER</div><div>VERIDAN SERVICE</div></div>
    <div class="row teal" style="height:30px"><div class="fn"><svg viewBox="0 0 14 14" fill="none" stroke="currentColor" stroke-width="1.4"><circle cx="7" cy="7" r="5.5"/><circle cx="7" cy="7" r="2.5"/><path d="M7 7l5-5"/></svg>Sets Project Objectives</div><div class="svc">Develops Delivery Plans</div></div>
    <div class="row soft" style="height:30px"><div class="fn"><svg viewBox="0 0 14 14" fill="none" stroke="currentColor" stroke-width="1.4"><circle cx="7" cy="9.5" r="2.5"/><path d="M7 7V1.5M4 3.5L7 1l3 2.5M1.5 6h3M9.5 6h3"/></svg>Approves Major Decisions</div><div class="svc">Provides Recommendations</div></div>
    <div class="row teal" style="height:29px"><div class="fn"><svg viewBox="0 0 14 14" fill="none" stroke="currentColor" stroke-width="1.4"><path d="M7 1.5l5.5 10h-11z"/><path d="M7 5.5v3M7 10v.5"/></svg>Holds Project Risk</div><div class="svc">Identifies and Manages Risks</div></div>
    <div class="row soft" style="height:30px"><div class="fn"><svg viewBox="0 0 14 14" fill="none" stroke="currentColor" stroke-width="1.4"><rect x="2" y="1.5" width="9" height="11" rx="1"/><path d="M4 4.5h5M4 7h5M4 9.5h3"/></svg>Awards Contracts</div><div class="svc">Manages Contractor Interfaces</div></div>
    <div class="row teal" style="height:29px"><div class="fn"><svg viewBox="0 0 14 14" fill="none" stroke="currentColor" stroke-width="1.4"><circle cx="7" cy="5" r="3.5"/><path d="M1 12.5h12"/></svg>Provides Funding</div><div class="svc">Monitors Cost and Schedule Performance</div></div>
    <div class="row soft" style="height:30px"><div class="fn"><svg viewBox="0 0 14 14" fill="none" stroke="currentColor" stroke-width="1.4"><rect x="1.5" y="2.5" width="9" height="9" rx="1"/><path d="M1.5 5.5h9"/><circle cx="10.5" cy="10.5" r="2.5" fill="#efefef"/></svg>Scheduling</div><div class="svc">Master Schedule Development, WBS,<br>Resource Allocation, Monitoring &amp; Updating</div></div>
  </div>

  <h2 class="abs head" style="top:268px"><b style="color:var(--teal)">PDP</b> Benefits</h2>
  <ul class="abs list good" style="top:290px">
    <li><i></i>Provides owners with access to experienced project delivery capability</li>
    <li><i></i>Improved project controls and governance</li>
    <li><i></i>Greater flexibility than traditional EPC delivery</li>
    <li><i></i>Enhanced visibility and management of cost, schedule and risk</li>
    <li><i></i>Scalable resources aligned with project phases</li>
  </ul>
  <div class="abs side-photo" style="top:268px;background:linear-gradient(180deg,#cfe0f2 0%,#7d9cc4 55%,#3d5a8a 100%)" role="img" aria-label="Photograph of a gas processing facility with blue steel columns"></div>

  <h2 class="abs head" style="top:368px"><b style="color:var(--teal)">PDP</b> Challenges</h2>
  <ul class="abs list bad" style="top:390px">
    <li><i></i>Owner retains significant delivery risk</li>
    <li><i></i>Requires clear governance and decision-making processes</li>
    <li><i></i>Multiple contractor interfaces require strong coordination</li>
    <li><i></i>Success depends on collaborative Owner-PDP relationship</li>
  </ul>
  <div class="abs side-photo" style="top:362px;background:linear-gradient(180deg,#a8c3de 0%,#9aa4ad 50%,#5b636b 100%)" role="img" aria-label="Photograph of stainless steel process vessels and pipework"></div>

  <div class="abs contact"><span>For More Information Contact:</span><span>directors@veridan.com.au</span></div>
  <div class="abs footer"><span class="globe"></span><span class="url">www.veridan.com.au</span><span class="rule"></span><span class="num">04</span></div>
</section>

</body>
</html>
```